Web and Mobile banner ad designs for bravlo

I need both web and mobile ad designs for the launch of a new app called bravlo.

These are the sizes that I am looking at for both the web and mobile banners:

1) WEB banner - static
728 x 90
300 x 250

2) MOBILE banner - static
320 x 50 Pixels XX-Large Image Banner
300 x 50 Pixels X-Large Image Banner
216 x 36 Pixels Large Image Banner
168 x 28 Pixels Medium Image Banner
120 x 20 Pixels Small Image Banner

Format: jpeg, png, gif

Copy: I have 2 versions of copy that I need for each of the banner sizes as listed above.

Copy 1:
Lazy to text? Send voice messages in just 1 click.
Download bravlo now!

Copy 2:
Turn your phone into a walkie talkie. bravlo!
Download the free app today!

Reason: Extending timeline so that I can provide designers with more time to think this through.

Hi All,
I have just extended the deadline to this brief and has up my contest prize amount.
I have also uploaded a mock up of what the app website will look like.

Any further questions, please feel free to give me a shout.

Thanks for your interest.

Hi,
I am working on a launch of a new app with its core feature - voice messaging.
I need banner ads for both mobile and online, details are within the brief.

I need a very strong designer to help me out here with the banner design to "vamp" up my product.

Any questions, please feel free to give me a shout.

Thanks all for your interest.

Reason: Extended the timeline as I couldn't get the design that I wanted

Target Market(s)

Anyone who has a Quindral account can use this app to communicate to their friends. It works like a walkie talkie.

Requirements
Must have
• 1) bravlo logo

```html
<!DOCTYPE html>
<html lang="en">
<head>
<meta charset="utf-8">
<title>bravlo web banner 728x90</title>
<link rel="stylesheet" href="https://fonts.googleapis.com/css2?family=Arimo:wght@400;700&display=swap">
<style>
  :root {
    --banner-top: #ffffff;
    --banner-bottom: #d9d9d9;
    --banner-border: #9a9a9a;
    --brand-red: #d8261c;
    --copy-ink: #111111;
  }
  html, body {
    margin: 0;
    padding: 0;
    width: 1200px;
    height: 148px;
    overflow: hidden;
    background: #ffffff;
  }
  .banner {
    position: relative;
    box-sizing: border-box;
    width: 1200px;
    height: 148px;
    border: 2px solid var(--banner-border);
    background: linear-gradient(to bottom, var(--banner-top) 0%, var(--banner-top) 45%, var(--banner-bottom) 100%);
    font-family: "Arimo", Arial, sans-serif;
    overflow: hidden;
  }
  .brand {
    position: absolute;
    left: 14px;
    top: 26px;
    display: flex;
    align-items: center;
    gap: 7px;
  }
  .brand-dot {
    width: 24px;
    height: 24px;
    border-radius: 50%;
    background: var(--brand-red);
  }
  .brand-name {
    font-weight: 700;
    font-size: 30px;
    color: var(--brand-red);
    letter-spacing: -0.5px;
  }
  .copy {
    position: absolute;
    left: 185px;
    right: 14px;
    top: 18px;
    margin: 0;
    color: var(--copy-ink);
    font-weight: 700;
    font-size: 15px;
    line-height: 26px;
  }
  .copy-line {
    display: block;
    white-space: nowrap;
  }
  .copy-cta {
    color: var(--brand-red);
  }
</style>
</head>
<body>
  <div class="banner">
    <div class="brand">
      <span class="brand-dot"></span>
      <span class="brand-name">bravlo</span>
    </div>
    <p class="copy">
      <span class="copy-line">Lazy to text? Send voice messages in just 1 click.</span>
      <span class="copy-line">Turn your phone into a walkie talkie. bravlo!</span>
      <span class="copy-line">Anyone with a Quindral account can talk to friends instantly.</span>
      <span class="copy-line copy-cta">Download bravlo now! Download the free app today!</span>
    </p>
  </div>
</body>
</html>
```